Brightgate Homes is a company designed to assist distressed homeowners short sell their property

Brightgate Homes is a company designed to assist distressed homeowners liquidate their real properties for less than is owed on their mortgage. We help consumers through a stressful and difficult period of time by becoming their liaisons and advocates. We work with mortgage lenders to negotiate a reduced payoff amount that will satisfy all parties involved including the buyer, seller, and junior lien holders.

Target Market(s)

Distressed homeowner, Real estate Brokers & Agents

Industry/Entity Type

Real Estate

Coding

Coded - Design and coding required

Number of Pages Required

3 page

Font styles to use
Sans Serif

Requirements
Must have
• Small, simple, and elegant header. Must have a large photo under the header that fits within the screen, without having to scroll down to view the entire image. It should include a few simple words on the cover photo with a call to action, that does not cover the intended image or placed on the side. Under the large photo, we would like to have the ability to add additional content that can be a preview to other pages. This content would be viewed by scrolling down. We would like colors that work well with our logo. We are also requesting that the design be coded and fully developed in WordPress. Our current domain is purchased, brightgatehomes.example and will be hosted by NetHarbor.
Nice to have
• Example website: https://www.pixelmarsh.example/photos/about/?page=home or http://www.quillvane.example/ or https://www.tovaro.example/. We like to have the picture on the first page have some sort of action, such as zooming in to the picture.
Should not have
• Should not have too many variant colors. Should not feel too busy. No pop-ups.

```html
<!DOCTYPE html>
<html lang="en">
<head>
<meta charset="utf-8">
<title>Brightgate Homes</title>
<link rel="stylesheet" href="https://fonts.googleapis.com/css2?family=Open+Sans:wght@300;400;600;700&family=Roboto+Slab:wght@700&display=swap">
<style>
:root{
  --orange:#e8772e;
  --blue:#3e64ad;
  --ink:#222;
  --text:#666;
  --band:#ebebeb;
  --footer:#1d1d1d;
  --white:#fff;
}
*{box-sizing:border-box;margin:0;padding:0}
html,body{width:1200px;height:2216px;overflow:hidden}
body{font-family:"Open Sans",Arial,sans-serif;color:var(--text);background:var(--white);position:relative}

.hero{position:absolute;left:0;top:0;width:1200px;height:716px;overflow:hidden}
.hero-photo{position:absolute;inset:0;background:linear-gradient(180deg,#9fb2c4 0%,#c9c1b2 35%,#8d8a7c 65%,#3e4a3c 100%)}
.hero-shade{position:absolute;inset:0;background:linear-gradient(180deg,rgba(0,0,0,.35) 0,rgba(0,0,0,0) 90px,rgba(0,0,0,0) 380px,rgba(0,0,0,.55) 100%)}
.site-header{position:absolute;left:0;top:0;width:100%;height:70px;display:flex;align-items:center;justify-content:space-between;padding:0 36px 0 24px}
.brand{display:flex;align-items:center;gap:10px;color:var(--white);font-weight:600;font-size:20px}
.brand-mark{width:22px;height:22px;background:var(--orange)}
.main-nav{display:flex;gap:26px}
.main-nav a{color:var(--white);text-decoration:none;font-size:15px;font-weight:600;padding-bottom:4px}
.main-nav a.active{border-bottom:2px solid var(--orange)}
.hero-text{position:absolute;left:0;right:0;top:500px;text-align:center;color:var(--white);font-weight:300;font-size:38px;line-height:50px}
.hero-arrow{position:absolute;left:570px;top:640px}

.features{position:absolute;left:0;top:716px;width:1200px;height:544px}
.section-title{font-family:"Roboto Slab",Georgia,serif;font-weight:700;color:var(--ink);font-size:32px;text-align:center;position:absolute;left:0;right:0;top:44px}
.feature{position:absolute;top:140px;width:280px;text-align:center}
.feature h3{font-size:18px;color:var(--ink);font-weight:700;margin-bottom:14px}
.feature-photo{width:280px;height:155px;margin-bottom:16px}
.feature p{font-size:12.5px;line-height:19px}
.promo{position:absolute;left:770px;top:152px;width:288px;height:340px;background:var(--blue);color:var(--white);text-align:center;padding-top:22px}
.promo h3{font-size:27px;font-weight:700}
.promo p{font-size:12.5px;margin-top:4px;opacity:.9}
.promo-art{width:240px;height:170px;margin:16px auto 0;background:linear-gradient(135deg,#7f9bd0,#d8dde6 60%,#c98a52)}
.btn{display:inline-block;background:var(--orange);color:var(--white);font-size:13px;font-weight:600;padding:9px 20px;border-radius:2px}
.promo .btn{margin-top:18px}

.listings{position:absolute;left:0;top:1260px;width:1200px;height:350px;background:var(--band)}
.listing{position:absolute;top:44px;width:212px;height:280px;overflow:hidden}
.listing-photo{position:absolute;inset:0}
.listing-info{position:absolute;left:0;right:0;top:110px;text-align:center;color:var(--white);padding:0 8px}
.price{display:inline-block;background:var(--orange);font-size:12px;font-weight:700;padding:3px 12px;margin-bottom:8px}
.listing-info h4,.listing-info .address{display:block;font-family:"Roboto Slab",Georgia,serif;font-size:22px;line-height:26px;font-weight:700;text-shadow:0 1px 3px rgba(0,0,0,.5)}
.listing-info h4{text-transform:uppercase}

.info{position:absolute;left:0;top:1610px;width:1200px;height:510px}
.why{position:absolute;left:145px;top:50px;width:210px}
.why h3,.faq h3{font-size:18px;color:var(--ink);font-weight:700;margin-bottom:14px}
.why p{font-size:12.5px;line-height:19px;margin-bottom:14px}
.why p strong{color:var(--ink)}
.faq{position:absolute;left:380px;top:50px;width:440px}
.faq-item{border:1px solid #ddd;margin-bottom:8px;font-size:12.5px}
.faq-q{padding:11px 14px;display:flex;gap:10px;align-items:center;color:var(--ink);font-weight:600}
.faq-q::before{content:"+";color:var(--orange);font-weight:700}
.faq-item.open .faq-q{background:#eef1f8;color:var(--blue)}
.faq-item.open .faq-q::before{content:"–"}
.faq-a{padding:12px 16px;line-height:19px}
.loan{position:absolute;left:845px;top:50px;width:210px;text-align:center}
.loan-art{width:170px;height:140px;margin:0 auto;background:linear-gradient(160deg,var(--blue),#a9b8d8);position:relative}
.loan-rate{position:absolute;right:-8px;top:-8px;width:62px;height:62px;border-radius:50%;background:var(--blue);color:var(--white);font-size:24px;font-weight:700;line-height:56px;border:3px solid var(--white)}
.loan h3{color:var(--orange);font-size:24px;font-weight:700;margin:14px 0 8px}
.loan p{font-size:12.5px;line-height:19px}

.site-footer{position:absolute;left:0;top:2130px;width:1200px;height:86px;background:var(--footer);display:flex;align-items:center;justify-content:space-between;padding:0 145px;color:#aaa;font-size:13px}
.to-top{width:40px;height:40px;background:var(--white);display:flex;align-items:center;justify-content:center}
</style>
</head>
<body>

<section class="hero">
  <div class="hero-photo" role="img" aria-label="Smiling real estate agent holding house keys in front of a suburban home"></div>
  <div class="hero-shade"></div>
  <header class="site-header">
    <div class="brand"><span class="brand-mark"></span>Brightgate Homes</div>
    <nav class="main-nav">
      <a href="#" class="active">Home</a><a href="#">About</a><a href="#">Property</a><a href="#">Services</a><a href="#">Contact</a>
    </nav>
  </header>
  <p class="hero-text">We assist homeowners liquidate their real properties for<br>less than is owed on their mortgage.</p>
  <svg class="hero-arrow" width="60" height="30" viewBox="0 0 60 30"><polyline points="4,4 30,26 56,4" fill="none" stroke="#fff" stroke-width="3"/></svg>
</section>

<section class="features">
  <h2 class="section-title">The easiest way to find property</h2>
  <div class="feature" style="left:145px">
    <h3>Home managers</h3>
    <div class="feature-photo" role="img" aria-label="Family meeting a home manager at their front door" style="background:linear-gradient(135deg,#b9a489,#e6ddd0 55%,#8c7a66)"></div>
    <p>Our managers look after your home while it is on the market. We handle showings, repairs and paperwork so you can focus on your next step with less stress and more time.</p>
  </div>
  <div class="feature" style="left:460px">
    <h3>Realtor</h3>
    <div class="feature-photo" role="img" aria-label="Realtor handing over house keys" style="background:linear-gradient(135deg,#c8d6c0,#eef0e6 55%,#9fb28e)"></div>
    <p>Our trusted realtors list your property, talk with your lender and find the right buyer. They stay with you from the first call until the final papers are signed and closed.</p>
  </div>
  <div class="promo">
    <h3>Free removal</h3>
    <p>Stay near your home. We move the rest.</p>
    <div class="promo-art" role="img" aria-label="Moving van with stacked boxes and a zero dollar badge"></div>
    <span class="btn">Learn more</span>
  </div>
</section>

<section class="listings">
  <div class="listing" style="left:145px">
    <div class="listing-photo" role="img" aria-label="Two-storey brick house" style="background:linear-gradient(180deg,#6f8fb8,#a87a55 60%,#4b5a3a)"></div>
    <div class="listing-info"><span class="price">$320,000</span><h4>Alder Crest</h4><span class="address">12 Fernwell Lane</span></div>
  </div>
  <div class="listing" style="left:377px">
    <div class="listing-photo" role="img" aria-label="Stone house with garden" style="background:linear-gradient(180deg,#4d6f95,#8a8478 60%,#3d4a34)"></div>
    <div class="listing-info"><span class="price">$285,000</span><h4>Mapleton</h4><span class="address">48 Quarry Walk</span></div>
  </div>
  <div class="listing" style="left:609px">
    <div class="listing-photo" role="img" aria-label="Modern suburban house" style="background:linear-gradient(180deg,#4a7ec4,#9a7a5c 60%,#5c6a48)"></div>
    <div class="listing-info"><span class="price">$410,000</span><h4>Harrowfield</h4><span class="address">715 Linden Rd</span></div>
  </div>
  <div class="listing" style="left:841px">
    <div class="listing-photo" role="img" aria-label="Family house with green lawn" style="background:linear-gradient(180deg,#9fc1de,#8b8c86 55%,#5e8a3c)"></div>
    <div class="listing-info"><span class="price">$265,000</span><h4>Oakvale</h4><span class="address">27 Birchmere Ave</span></div>
  </div>
</section>

<section class="info">
  <div class="why">
    <h3>Why us?</h3>
    <p><strong>We guide you through every step of a short sale, with calm and honest advice.</strong></p>
    <p>We speak with your lender, answer their questions and keep the sale moving. Our team knows how to reach a fair payoff that works for everyone.</p>
    <p>You get one clear contact, fast replies and no hidden fees along the way.</p>
    <span class="btn">Read more</span>
  </div>
  <div class="faq">
    <h3>Questions &amp; answers</h3>
    <div class="faq-item open">
      <div class="faq-q">What is a short sale and who is it for?</div>
      <div class="faq-a">A short sale lets you sell your home for less than the loan balance. Your lender agrees to accept the lower amount, and you avoid foreclosure. It is a good fit for owners facing hardship who want a fresh start.</div>
    </div>
    <div class="faq-item"><div class="faq-q">How long does the process take?</div></div>
    <div class="faq-item"><div class="faq-q">Will my credit be affected?</div></div>
    <div class="faq-item"><div class="faq-q">Do I pay any fees up front?</div></div>
  </div>
  <div class="loan">
    <div class="loan-art" role="img" aria-label="House with a percentage badge"><span class="loan-rate">7%</span></div>
    <h3>Housing loan</h3>
    <p>Ask about low rate loans for your next home. We help you compare offers and plan the move.</p>
  </div>
</section>

<footer class="site-footer">
  <span>© 2015 Brightgate Homes. All Rights Reserved.</span>
  <span class="to-top"><svg width="16" height="10" viewBox="0 0 16 10"><polyline points="2,8 8,2 14,8" fill="none" stroke="#333" stroke-width="2"/></svg></span>
</footer>

</body>
</html>
```